Rimah Advertising & Publicity business cards

I would like my Company's business card to be designed creatively & profissionally the logo is attached in both Arabic & english and prefer to have my emblem dimmed on the card as well
-Logo ( Arabic & English)
-Name (Arabic & English)
-Title ( Arabic & English)
-----------
-Location
-Landline (icon)
-Mobile phone (icon)
-Email (icon)
-Instagram (icon)
-WhatsApp (icon)

Target Market(s)

Industry/Entity Type

Marketing

Contact Information for Business Card

-Logo ( Arabic & English)
-Name (Arabic & English)
-----------
-Location
-Landline (icon)
-Mobile phone (icon)
-Email (icon)
-Instagram (icon)
-WhatsApp (icon)

Font styles to use
Serif

Requirements
Must have
• all what is mentions in business card details blanked and i will add the data my self
Nice to have
• Dim emblem on my business card both Arabic & english

```html
<!DOCTYPE html>
<html lang="en">
<head>
<meta charset="utf-8">
<title>Rimah Advertising &amp; Publicity – Business Cards</title>
<link rel="stylesheet" href="https://fonts.googleapis.com/css2?family=Lora:wght@400;500;700&family=Amiri:wght@400;700&display=swap">
<style>
  :root {
    --backdrop: #2b2b2c;
    --card: #1b1b1c;
    --card-edge: #101011;
    --ink: #f2f2f2;
    --ink-soft: #d4d4d4;
    --teal: #3cc6c0;
    --rule: #5f5f5f;
    --ghost: rgba(255,255,255,.05);
  }
  * { margin: 0; padding: 0; box-sizing: border-box; }
  html, body { width: 1200px; height: 900px; overflow: hidden; }
  body {
    background: var(--backdrop);
    font-family: "Lora", Georgia, serif;
    color: var(--ink);
    position: relative;
  }
  .card {
    position: absolute;
    top: 300px;
    width: 520px;
    height: 300px;
    background: var(--card);
    border-radius: 22px;
    overflow: hidden;
    box-shadow: 0 6px 0 var(--card-edge), 0 14px 30px rgba(0,0,0,.45);
  }
  .card--front { left: 50px; }
  .card--back { left: 630px; }

  .ghost-name {
    position: absolute;
    color: var(--ghost);
    line-height: 1;
    white-space: nowrap;
    pointer-events: none;
  }
  .ghost-name--en { left: 26px; bottom: 14px; font-size: 84px; font-weight: 400; }
  .ghost-name--ar { right: 30px; bottom: -6px; font-family: "Amiri", "Lora", serif; font-size: 110px; }

  /* Front: brand block */
  .brand {
    position: absolute;
    left: 36px;
    top: 112px;
    display: flex;
    align-items: center;
  }
  .brand__mark {
    width: 40px; height: 40px;
    background: var(--teal);
    border-radius: 4px;
    margin-right: 14px;
  }
  .brand__rule {
    width: 1px; height: 58px;
    background: var(--rule);
    margin-right: 12px;
  }
  .brand__name { font-size: 34px; font-weight: 400; line-height: 1; }
  .brand__tag { font-size: 10.5px; color: var(--ink-soft); margin-top: 7px; }

  .divider {
    position: absolute;
    left: 276px;
    top: 30px;
    width: 1px;
    height: 240px;
    background: var(--rule);
  }

  /* Front: contact block */
  .contact {
    position: absolute;
    left: 294px;
    top: 26px;
    width: 210px;
    font-size: 12px;
    line-height: 1.35;
    color: var(--ink-soft);
  }
  .contact__name { font-size: 18px; font-weight: 700; color: var(--ink); line-height: 1.2; }
  .contact__name-ar, .contact__title-ar {
    font-family: "Amiri", "Lora", serif;
    direction: rtl;
    text-align: left;
  }
  .contact__name-ar { font-size: 15px; color: var(--ink); line-height: 1.3; }
  .contact__title { color: var(--teal); }
  .contact__title-ar { font-size: 13px; color: var(--teal); line-height: 1.3; margin-bottom: 7px; }
  .contact__address { margin-bottom: 7px; }
  .contact__row { display: flex; align-items: center; height: 17px; }
  .contact__icon {
    width: 11px; height: 11px;
    margin-right: 7px;
    flex: none;
    fill: none;
    stroke: var(--teal);
    stroke-width: 1.6;
  }
  .contact__dot {
    width: 9px; height: 9px;
    margin: 0 8px 0 1px;
    border-radius: 50%;
    background: var(--teal);
    flex: none;
  }

  /* Back */
  .back-brand {
    position: absolute;
    left: 0; right: 0;
    top: 100px;
    display: flex;
    justify-content: center;
    align-items: center;
  }
  .back-brand__text {
    font-family: "Amiri", "Lora", serif;
    text-align: right;
    direction: rtl;
  }
  .back-brand__name { font-size: 46px; font-weight: 700; line-height: 1.1; }
  .back-brand__tag { font-size: 15px; color: var(--ink-soft); line-height: 1.2; }
  .back-brand__rule {
    width: 1px; height: 70px;
    background: var(--rule);
    margin: 0 14px;
  }
  .back-brand__mark {
    width: 46px; height: 46px;
    background: var(--teal);
    border-radius: 4px;
  }
</style>
</head>
<body>

<section class="card card--front" aria-label="Business card front">
  <div class="ghost-name ghost-name--en" aria-hidden="true">Rimah</div>

  <div class="brand">
    <div class="brand__mark"></div>
    <div class="brand__rule"></div>
    <div>
      <div class="brand__name">Rimah</div>
      <div class="brand__tag">Advertising and Publicity</div>
    </div>
  </div>

  <div class="divider"></div>

  <div class="contact">
    <div class="contact__name">Daniel Harper</div>
    <div class="contact__name-ar" lang="ar">دانيال هاربر</div>
    <div class="contact__title">Managing Director</div>
    <div class="contact__title-ar" lang="ar">المدير العام</div>
    <div class="contact__address">12345, Address Goes Here<br>Country Name, 123456.</div>

    <div class="contact__row">
      <svg class="contact__icon" viewBox="0 0 12 12" aria-label="Landline"><path d="M2.5 1h2l1 2.5-1.3 1a6 6 0 0 0 3.3 3.3l1-1.3 2.5 1v2a1 1 0 0 1-1 1A9.5 9.5 0 0 1 1.5 2a1 1 0 0 1 1-1z"/></svg>
      044-555 018 230
    </div>
    <div class="contact__row">
      <svg class="contact__icon" viewBox="0 0 12 12" aria-label="Mobile"><rect x="3" y="0.8" width="6" height="10.4" rx="1.2"/><path d="M5.2 9.2h1.6"/></svg>
      050-555 014 2
    </div>
    <div class="contact__row">
      <svg class="contact__icon" viewBox="0 0 12 12" aria-label="Email"><rect x="0.8" y="2.2" width="10.4" height="7.6" rx="1"/><path d="M1 2.6l5 4 5-4"/></svg>
      info@rimahads.com
    </div>
    <div class="contact__row">
      <svg class="contact__icon" viewBox="0 0 12 12" aria-label="Website"><circle cx="6" cy="6" r="5"/><path d="M1 6h10M6 1c-2.2 2.8-2.2 7.2 0 10M6 1c2.2 2.8 2.2 7.2 0 10"/></svg>
      www.rimahads.com
    </div>
    <div class="contact__row"><span class="contact__dot" aria-label="Instagram"></span>@rimahads</div>
    <div class="contact__row"><span class="contact__dot" aria-label="WhatsApp"></span>+971 50 555 0142</div>
  </div>
</section>

<section class="card card--back" aria-label="Business card back">
  <div class="ghost-name ghost-name--ar" lang="ar" aria-hidden="true">ريماه</div>
  <div class="back-brand">
    <div class="back-brand__text" lang="ar">
      <div class="back-brand__name">ريماه</div>
      <div class="back-brand__tag">للدعاية والإعلان</div>
    </div>
    <div class="back-brand__rule"></div>
    <div class="back-brand__mark"></div>
  </div>
</section>

</body>
</html>
```